Trucking company specializing in intermodal containers

We need a logo design for our trucking company based in Kent, Washington. Our companies name is Varnell Haulways LLC, we specialize in intermodal containers, and work off of the Crestmark Rail Lines and the ports. We provide service by transporting freight with our fleet of trucks. We operate within Washington, Oregon, and Idaho. Our fleet consists of an east division and a local division. Our team motto currently is globally connected, locally invested.

Target Market(s)

brokers, intermodal management companies, customers

Industry/Entity Type

Trucking Company

Contact Information for Business Card

physical address 4153 N. 318th Pl Kent, WA 98417
office number is 253-555-0148

Font styles to use
Sans Serif

Colors

Designer to choose colors to be used in the design.

Requirements
Must have
• We need to update our current logo. Something like an emblem; that makes a statement that this logo/ sign represents Varnell Haulways. Something like a royal stamp but in this case a royal shield.
Nice to have
• simple, yet bold. something someone does not currently have. We need something fresh and exciting. Something that will also make a statement because currently our reputation is great within the industry and our community. But we need to reflect that we are professional and willing to provide the best service. We are open to new statement lines.
Should not have
• Should not have something thats been used before. We are open to suggestions that you have and a design that is completely unique and you make originally without what we want but what you like as well. Ofcourse it should still represent the industry we are in.

```html
<!DOCTYPE html>
<html lang="en">
<head>
<meta charset="utf-8">
<title>Varnell Haulways LLC — Business Card</title>
<link rel="stylesheet" href="https://fonts.googleapis.com/css2?family=Cinzel:wght@400&family=Tenor+Sans&display=swap">
<style>
  :root {
    --canvas: #e4e4e4;
    --card: #f7f7f6;
    --card-edge: #dcdcdc;
    --brand-red: #8b2b2b;
    --ink: #2b2b2b;
    --ink-soft: #555555;
    --slash: #d6d6d6;
  }
  * { box-sizing: border-box; margin: 0; padding: 0; }
  html, body { width: 1200px; height: 800px; overflow: hidden; }
  body {
    background: var(--canvas);
    display: flex;
    align-items: center;
    justify-content: center;
    gap: 60px;
    font-family: "Tenor Sans", sans-serif;
  }
  .card {
    position: relative;
    width: 525px;
    height: 300px;
    background: var(--card);
    border: 1px solid var(--card-edge);
    box-shadow: 0 2px 6px rgba(0,0,0,0.08);
    overflow: hidden;
  }

  /* Front face */
  .card-front {
    display: flex;
    align-items: center;
    justify-content: center;
  }
  .front-mark {
    display: flex;
    align-items: center;
    gap: 18px;
  }
  .mark-square {
    width: 34px;
    height: 34px;
    background: var(--brand-red);
  }
  .front-name {
    font-size: 30px;
    letter-spacing: 3px;
    color: var(--brand-red);
    text-transform: uppercase;
  }

  /* Back face */
  .slash-decor {
    position: absolute;
    left: 205px;
    top: 95px;
    width: 80px;
    height: 190px;
    background: linear-gradient(160deg, rgba(214,214,214,0) 0%, var(--slash) 50%, rgba(214,214,214,0) 100%);
    opacity: 0.7;
  }
  .back-mark {
    position: absolute;
    left: 26px;
    top: 28px;
    display: flex;
    align-items: center;
    gap: 8px;
  }
  .back-mark .mark-square { width: 16px; height: 16px; }
  .back-mark-name {
    font-size: 12px;
    letter-spacing: 1px;
    color: var(--brand-red);
    text-transform: uppercase;
    line-height: 1.2;
    width: 110px;
  }
  .company-heading {
    position: absolute;
    left: 175px;
    top: 26px;
    right: 28px;
    font-family: "Cinzel", serif;
    font-size: 17px;
    letter-spacing: 2px;
    color: var(--brand-red);
    padding-bottom: 4px;
    border-bottom: 1px solid var(--brand-red);
  }
  .contact {
    position: absolute;
    left: 220px;
    top: 66px;
    letter-spacing: 2.5px;
  }
  .person-name { font-size: 19px; color: var(--brand-red); }
  .person-role { font-size: 17px; color: var(--ink); margin-left: 72px; margin-bottom: 12px; }
  .label { font-size: 14px; color: var(--brand-red); line-height: 1.25; }
  .value { font-size: 14px; color: var(--ink); line-height: 1.25; }
  .website { font-size: 14px; color: var(--ink); margin-top: 14px; margin-left: 30px; letter-spacing: 4px; }
</style>
</head>
<body>
  <section class="card card-front" aria-label="Business card front">
    <div class="front-mark">
      <span class="mark-square"></span>
      <span class="front-name">Varnell Haulways</span>
    </div>
  </section>

  <section class="card card-back" aria-label="Business card back">
    <div class="slash-decor" role="img" aria-label="Faint grey slash decoration"></div>
    <div class="back-mark">
      <span class="mark-square"></span>
      <span class="back-mark-name">Varnell Haulways</span>
    </div>
    <h1 class="company-heading">VARNELL HAULWAYS LLC.</h1>
    <div class="contact">
      <p class="person-name">Daniel Reyes</p>
      <p class="person-role">President</p>
      <p class="label">Physical Address</p>
      <p class="value">4153 N. 318th Pl Kent</p>
      <p class="value">WA 98417</p>
      <p class="label">Office number</p>
      <p class="value">253-555-0148</p>
      <p class="website">www.varnellhaulways.com</p>
    </div>
  </section>
</body>
</html>
```